Tirovel

We need a business card for our company is a holding for different business all are different we try to have some air of relax and fun in our projects we add pictures of the office to give you an idea od the mood of the business

Business

```html
<!DOCTYPE html>
<html lang="en">
<head>
<meta charset="utf-8">
<title>Tirovel — Business Card</title>
<link rel="stylesheet" href="https://fonts.googleapis.com/css2?family=Oswald:wght@400&display=swap">
<style>
  :root {
    --card-yellow: #f2d800;
    --lemon: #f4f41c;
    --cream-white: #ffffff;
    --ink: #231400;
    --band-yellow: #eef22a;
    --band-text: #7b5a06;
    --divider: #f8f8b0;
  }
  * { margin: 0; padding: 0; box-sizing: border-box; }
  html, body {
    width: 1200px;
    height: 720px;
    overflow: hidden;
    background: var(--card-yellow);
  }
  .card {
    position: relative;
    width: 1200px;
    height: 720px;
    background: var(--card-yellow);
    font-family: "Oswald", "Arial Narrow", sans-serif;
    font-weight: 400;
    color: var(--ink);
    overflow: hidden;
  }
  .card__swoosh {
    position: absolute;
    left: 0;
    top: 0;
    width: 1200px;
    height: 720px;
  }
  .company-name {
    position: absolute;
    left: 58px;
    top: 70px;
    font-size: 110px;
    font-weight: 400;
    line-height: 1;
    color: var(--ink);
  }
  .holder {
    position: absolute;
    right: 34px;
    top: 28px;
    text-align: right;
  }
  .holder__name {
    font-size: 38px;
    line-height: 1.2;
  }
  .holder__role {
    font-size: 25px;
    line-height: 1.2;
    margin-top: 2px;
  }
  .contact {
    position: absolute;
    left: 715px;
    top: 498px;
    list-style: none;
    font-size: 27px;
    line-height: 51px;
  }
  .website {
    position: absolute;
    left: 43px;
    top: 602px;
    font-size: 27px;
  }
  .ventures {
    position: absolute;
    left: 0;
    bottom: 0;
    width: 1200px;
    height: 52px;
    background: var(--band-yellow);
    display: flex;
    align-items: center;
    justify-content: center;
    list-style: none;
    padding-right: 10px;
  }
  .ventures__item {
    font-size: 26px;
    color: var(--band-text);
    padding: 0 28px;
    border-left: 2px solid var(--divider);
    line-height: 34px;
  }
  .ventures__item:first-child { border-left: none; }
</style>
</head>
<body>
  <main class="card">
    <svg class="card__swoosh" viewBox="0 0 1200 720" aria-hidden="true">
      <path d="M0 0 H915 C905 250 640 485 0 490 Z" fill="var(--cream-white)"/>
      <path d="M0 0 H670 C630 190 460 292 0 298 Z" fill="var(--lemon)"/>
    </svg>

    <h1 class="company-name">Tirovel</h1>

    <div class="holder">
      <p class="holder__name">Your Name</p>
      <p class="holder__role">Designation</p>
    </div>

    <ul class="contact">
      <li>Office Address :</li>
      <li>Contact No. :</li>
      <li>e-mail :</li>
    </ul>

    <p class="website">Visit us at : www.tirovel.com</p>

    <ul class="ventures">
      <li class="ventures__item">business name</li>
      <li class="ventures__item">business name</li>
      <li class="ventures__item">business name</li>
      <li class="ventures__item">business name</li>
      <li class="ventures__item">business name</li>
    </ul>
  </main>
</body>
</html>
```